Real State Agency App

We need an app design for a real state agency, we provide mockups for our project that ilustrates very well what we need
our web site is www.brightkeyhomes-example.com,

Target Market(s)

Tourism

Font styles to use
Other font styles liked:
• attached you will find it

Requirements
Must have
• Colors like the logo

```html
<!DOCTYPE html>
<html lang="en">
<head>
<meta charset="utf-8">
<title>View Property</title>
<link href="https://fonts.googleapis.com/css2?family=Montserrat:wght@400;500;600;700&family=Open+Sans:wght@400;600&display=swap" rel="stylesheet">
<style>
:root{
  --brand-blue:#0b93d6;
  --brand-cyan:#17c3d3;
  --amber:#f0b429;
  --page-bg:#e8eef1;
  --card-bg:#ffffff;
  --ink:#2b2f33;
  --muted:#44484c;
  --line:#e3e6e8;
  --tab-grey:#6f7478;
  --photo-a:#7f9f5a;
  --photo-b:#93ad72;
}
*{box-sizing:border-box;margin:0;padding:0}
html,body{width:675px;height:1200px;overflow:hidden}
body{background:var(--page-bg);font-family:"Montserrat",sans-serif;color:var(--ink);position:relative}
.top-bar{position:absolute;left:0;top:0;width:675px;height:126px;background:var(--brand-blue);color:#fff}
.status-bar{height:36px;display:flex;align-items:center;justify-content:space-between;padding:0 12px;font-family:"Open Sans",sans-serif;font-size:22px;font-weight:600}
.status-left,.status-right{display:flex;align-items:center;gap:8px;width:200px}
.status-right{justify-content:flex-end}
.nav-row{position:absolute;top:36px;left:0;right:0;height:90px;display:flex;align-items:center;justify-content:center}
.nav-title{font-size:28px;font-weight:700}
.nav-back{position:absolute;left:20px;top:28px}
.nav-share{position:absolute;right:22px;top:20px}
.property-photo{position:absolute;left:0;top:126px;width:675px;height:427px;background:linear-gradient(135deg,var(--photo-b) 0%,var(--photo-a) 100%)}
.photo-arrow{position:absolute;top:178px}
.photo-arrow.prev{left:22px}
.photo-arrow.next{right:22px}
.price-tag{position:absolute;left:0;top:484px;width:203px;height:69px;background:var(--amber);color:#fff;font-size:24px;font-weight:700;display:flex;align-items:center;padding-left:22px}
.card{position:absolute;left:13px;width:648px;background:var(--card-bg);border-radius:5px}
.summary-card{top:569px;height:219px}
.property-title{font-size:35px;font-weight:700;line-height:43px;padding:20px 22px 0;height:129px;border-bottom:2px solid var(--line)}
.features{display:flex;height:90px}
.feature{flex:1;display:flex;align-items:center;justify-content:center;gap:12px;font-size:19px;color:var(--ink);border-left:2px solid var(--line)}
.feature:first-child{border-left:none}
.request-button{position:absolute;left:13px;top:805px;width:648px;height:99px;border-radius:5px;background:linear-gradient(90deg,var(--brand-blue),var(--brand-cyan));color:#fff;font-size:26px;font-weight:700;display:flex;align-items:center;justify-content:center;gap:18px}
.description-card{top:920px;height:300px;padding:22px 22px}
.section-label{font-size:25px;font-weight:700;margin-bottom:14px}
.description-text{font-family:"Open Sans",sans-serif;font-size:26px;line-height:40px;color:var(--muted)}
.tab-bar{position:absolute;left:0;top:1123px;width:675px;height:77px;background:#fff;border-top:2px solid var(--line);display:flex}
.tab{flex:1;display:flex;flex-direction:column;align-items:center;justify-content:flex-end;padding-bottom:8px;gap:6px;font-size:19px;color:var(--tab-grey)}
.tab.active{color:var(--brand-blue);font-weight:700}
</style>
</head>
<body>
<header class="top-bar">
  <div class="status-bar">
    <div class="status-left">
      <svg width="30" height="16" viewBox="0 0 30 16"><g fill="#fff"><rect x="0" y="11" width="5" height="5"/><rect x="7" y="8" width="5" height="8"/><rect x="14" y="4" width="5" height="12"/><rect x="21" y="0" width="5" height="16"/></g></svg>
      <span>Carrier</span>
      <svg width="24" height="18" viewBox="0 0 24 18"><path d="M12 17l-4-4a6 6 0 0 1 8 0zM4 9a11 11 0 0 1 16 0l-2 2a8 8 0 0 0-12 0zM0 5a17 17 0 0 1 24 0l-2 2A14 14 0 0 0 2 7z" fill="#fff"/></svg>
    </div>
    <span>9:41 AM</span>
    <div class="status-right">
      <svg width="12" height="20" viewBox="0 0 12 20"><path d="M1 5l10 10-5 4V1l5 4L1 15" fill="none" stroke="#fff" stroke-width="2"/></svg>
      <span>100%</span>
      <svg width="44" height="20" viewBox="0 0 44 20"><rect x="1" y="1" width="38" height="18" rx="4" fill="none" stroke="#fff" stroke-width="2"/><rect x="4" y="4" width="32" height="12" rx="2" fill="#fff"/><rect x="41" y="7" width="3" height="6" rx="1" fill="#fff"/></svg>
    </div>
  </div>
  <div class="nav-row">
    <svg class="nav-back" width="34" height="32" viewBox="0 0 34 32"><path d="M32 16H4M16 3L3 16l13 13" fill="none" stroke="#fff" stroke-width="3.5" stroke-linecap="round" stroke-linejoin="round"/></svg>
    <span class="nav-title">View Property</span>
    <svg class="nav-share" width="30" height="40" viewBox="0 0 30 40"><path d="M15 25V3M8 10l7-7 7 7M10 15H3v23h24V15h-7" fill="none" stroke="#fff" stroke-width="2.5" stroke-linejoin="round"/></svg>
  </div>
</header>

<div class="property-photo" role="img" aria-label="Property photo: white villa with a garden lawn and trees">
  <svg class="photo-arrow prev" width="18" height="34" viewBox="0 0 18 34"><path d="M15 3L3 17l12 14" fill="none" stroke="#fff" stroke-width="3.5" stroke-linecap="round"/></svg>
  <svg class="photo-arrow next" width="18" height="34" viewBox="0 0 18 34"><path d="M3 3l12 14L3 31" fill="none" stroke="#fff" stroke-width="3.5" stroke-linecap="round"/></svg>
</div>
<div class="price-tag">1,000,000 €</div>

<section class="card summary-card">
  <h1 class="property-title">Villa Son Servera, Mallorca, Baleares</h1>
  <div class="features">
    <div class="feature">
      <svg width="30" height="22" viewBox="0 0 30 22"><g fill="none" stroke="#f0b429" stroke-width="2.2"><rect x="2" y="9" width="26" height="9"/><path d="M4 9V2h22v7M8 9V6h6v3M16 9V6h6v3M3 18v3M27 18v3"/></g></svg>
      <span>4 Bedrooms</span>
    </div>
    <div class="feature">
      <svg width="34" height="22" viewBox="0 0 34 22"><g fill="none" stroke="#f0b429" stroke-width="2.2"><path d="M1 4h32M4 4l3 14h20l3-14M8 18l-2 3M26 18l2 3"/></g></svg>
      <span>3 Bathrooms</span>
    </div>
    <div class="feature">
      <svg width="24" height="24" viewBox="0 0 24 24"><g fill="none" stroke="#f0b429" stroke-width="2.4" stroke-linecap="round"><path d="M3 21L21 3M11 3h10v10M3 11v10h10"/></g></svg>
      <span>206 (m²)</span>
    </div>
  </div>
</section>

<div class="request-button">
  <svg width="30" height="30" viewBox="0 0 30 30"><path d="M29 1L1 13l11 4 4 12z" fill="#fff"/></svg>
  <span>Send Request Information</span>
</div>

<section class="card description-card">
  <h2 class="section-label">Description</h2>
  <p class="description-text">Excellent opportunity. Villa in second line of the sea in the area of Son Servera, in the northeast of Mallorca. A magnificent area, very famous and is visited by many tourists during the summer months of</p>
</section>

<nav class="tab-bar">
  <div class="tab active">
    <svg width="30" height="30" viewBox="0 0 30 30"><g fill="none" stroke="#0b93d6" stroke-width="2.8" stroke-linecap="round"><circle cx="17" cy="12" r="9"/><path d="M10 19l-7 8"/></g></svg>
    <span>Search</span>
  </div>
  <div class="tab">
    <svg width="30" height="30" viewBox="0 0 30 30"><g fill="none" stroke="#6f7478" stroke-width="2.4" stroke-linejoin="round"><path d="M16 2h11v11L14 27 2 15z"/><circle cx="21" cy="8" r="2"/></g></svg>
    <span>Sell</span>
  </div>
  <div class="tab">
    <svg width="30" height="30" viewBox="0 0 30 30"><g fill="none" stroke="#6f7478" stroke-width="2.4"><circle cx="15" cy="15" r="4.5"/><path d="M13 2h4l1 4 3 1.5 3.5-2 3 3-2 3.5 1.2 3 4 1v4l-4 1-1.2 3 2 3.5-3 3-3.5-2-3 1.2-1 4h-4l-1-4-3-1.2-3.5 2-3-3 2-3.5L6 18l-4-1v-4l4-1 1.2-3-2-3.5 3-3 3.5 2L13 6z" transform="scale(.93) translate(1 1)"/></g></svg>
    <span>Our Services</span>
  </div>
  <div class="tab">
    <svg width="32" height="30" viewBox="0 0 32 30"><g fill="#6f7478"><path d="M2 2h28v20H12l-7 6v-6H2z" fill="none" stroke="#6f7478" stroke-width="2.4" stroke-linejoin="round"/><circle cx="10" cy="12" r="2"/><circle cx="16" cy="12" r="2"/><circle cx="22" cy="12" r="2"/></g></svg>
    <span>Contact</span>
  </div>
</nav>
</body>
</html>
```